Life Coach for Lawyers Business Card Design

Elegant, original, business card design for life coaching service for associate attorneys who work in big law and struggle with stress, overwhelm, and time management. Double sided design.

Target Market(s)

Women associate attorneys who work in big law and struggle with stress, overwhelm, and time management.

Industry/Entity Type

Life Coaching

Contact Information for Business Card

Marissa Pendrell
Life Coach
518.677.3941
calmbriefcounsel.net
marissa@calmbriefcounsel.net
@calmbriefcounsel (Instagram)

Font styles to use
Other font styles liked:
• Silver South font duo. See uploaded files.

Requirements
Must have
• Icons for phone, website, email, and Instagram instead of words. Specific colors used in my logo (171B2B, 421121, FFFFFF)
Nice to have
• Foil. Embossed. Feminine design.
Should not have
• Any colors other than those used in logo. See uploaded files.

```html
<!DOCTYPE html>
<html lang="en">
<head>
<meta charset="utf-8">
<title>Marissa Pendrell – Business Card</title>
<link rel="stylesheet" href="https://fonts.googleapis.com/css2?family=Lato:wght@300;400&family=Montserrat:wght@700&family=Raleway:wght@400&display=swap">
<style>
  :root {
    --plum: #2d0d22;
    --navy: #0c1427;
    --mist: #e4e4e4;
    --white: #ffffff;
  }
  html, body {
    margin: 0;
    padding: 0;
    width: 900px;
    height: 1200px;
    overflow: hidden;
    background: var(--navy);
  }
  .sheet {
    position: relative;
    width: 900px;
    height: 1200px;
    background: var(--navy);
  }
  .card {
    position: absolute;
    left: 0;
    width: 900px;
    height: 540px;
    overflow: hidden;
  }
  .card--front { top: 0; }
  .card--back { top: 660px; }
  .card__shapes {
    position: absolute;
    inset: 0;
    display: block;
  }
  .identity {
    position: absolute;
    left: 314px;
    top: 84px;
    color: var(--white);
  }
  .identity__name {
    margin: 0;
    font-size: 32px;
    line-height: 40px;
    white-space: nowrap;
  }
  .identity__first {
    font-family: "Montserrat", sans-serif;
    font-weight: 700;
    letter-spacing: -0.5px;
  }
  .identity__last {
    font-family: "Lato", sans-serif;
    font-weight: 300;
  }
  .identity__role {
    margin: 0 0 0 3px;
    font-family: "Lato", sans-serif;
    font-weight: 400;
    font-size: 22px;
    line-height: 26px;
  }
  .identity__rule {
    width: 197px;
    height: 2px;
    margin: 15px 0 0 3px;
    background: var(--navy);
  }
  .contact {
    position: absolute;
    left: 462px;
    margin: 0;
    padding: 0;
    list-style: none;
  }
  .contact__item {
    position: absolute;
    left: 0;
    display: flex;
    align-items: flex-start;
    width: 420px;
  }
  .contact__icon {
    flex: none;
    width: 37px;
    height: 37px;
    border: 1.5px solid var(--white);
    display: flex;
    align-items: center;
    justify-content: center;
  }
  .contact__text {
    margin-left: 26px;
    font-family: "Lato", sans-serif;
    font-weight: 400;
    font-size: 22px;
    line-height: 28px;
    color: var(--white);
    white-space: nowrap;
  }
  .contact__item--phone { top: 266px; }
  .contact__item--phone .contact__text { margin-top: 4px; }
  .contact__item--web { top: 338px; }
  .contact__item--web .contact__text { margin-top: -8px; }
  .contact__item--social { top: 410px; }
  .contact__item--social .contact__text { margin-top: -10px; }
  .site-link {
    position: absolute;
    left: 338px;
    top: 85px;
    display: flex;
    align-items: center;
    gap: 6px;
    font-family: "Raleway", sans-serif;
    font-weight: 400;
    font-size: 22px;
    color: var(--white);
  }
  .brand-seal {
    position: absolute;
    left: 544px;
    top: 248px;
    width: 248px;
    height: 248px;
    border: 1.5px solid var(--white);
    border-radius: 50%;
    box-sizing: border-box;
    display: flex;
    align-items: center;
    justify-content: center;
    text-align: center;
  }
  .brand-seal__name {
    font-family: "Lato", sans-serif;
    font-weight: 300;
    font-size: 26px;
    line-height: 34px;
    letter-spacing: 2px;
    color: var(--white);
  }
</style>
</head>
<body>
<main class="sheet">

  <section class="card card--front" aria-label="Card front">
    <svg class="card__shapes" viewBox="0 0 900 540" aria-hidden="true">
      <rect width="900" height="540" fill="var(--mist)"/>
      <path d="M184 0 C196 120 286 226 384 302 L52 540 L900 540 L900 0 Z" fill="var(--navy)"/>
      <path d="M202 0 C214 118 300 226 394 300 L148 540 L900 540 L900 0 Z" fill="var(--plum)"/>
      <path d="M800 76 C640 96 520 190 394 300 C530 200 650 110 800 76 Z" fill="var(--navy)" stroke="var(--navy)" stroke-width="3"/>
    </svg>

    <header class="identity">
      <h1 class="identity__name"><span class="identity__first">MARISSA</span> <span class="identity__last">Pendrell</span></h1>
      <p class="identity__role">Life Coach</p>
      <div class="identity__rule"></div>
    </header>

    <ul class="contact">
      <li class="contact__item contact__item--phone">
        <span class="contact__icon">
          <svg width="22" height="22" viewBox="0 0 24 24" aria-label="Phone" role="img">
            <path d="M3 8 C3 5 7 4 12 4 C17 4 21 5 21 8 L21 10 L17 10 L16 8 L8 8 L7 10 L3 10 Z" fill="var(--white)"/>
            <path d="M7 11 L17 11 L20 20 L4 20 Z" fill="var(--white)"/>
            <circle cx="12" cy="15.5" r="2.4" fill="var(--plum)"/>
          </svg>
        </span>
        <span class="contact__text">518.677.3941</span>
      </li>
      <li class="contact__item contact__item--web">
        <span class="contact__icon">
          <svg width="26" height="26" viewBox="0 0 24 24" aria-label="Website and email" role="img" fill="none" stroke="var(--white)" stroke-width="1.4">
            <circle cx="12" cy="12" r="9.5"/>
            <ellipse cx="12" cy="12" rx="4.2" ry="9.5"/>
            <line x1="2.5" y1="12" x2="21.5" y2="12"/>
            <path d="M4 7 H20 M4 17 H20"/>
          </svg>
        </span>
        <span class="contact__text">calmbriefcounsel.net<br>marissa@calmbriefcounsel.net</span>
      </li>
      <li class="contact__item contact__item--social">
        <span class="contact__icon">
          <svg width="22" height="22" viewBox="0 0 24 24" aria-label="Location" role="img" fill="none" stroke="var(--white)" stroke-width="1.6">
            <circle cx="12" cy="12" r="8"/>
          </svg>
        </span>
        <span class="contact__text">1847 Larkmoor Avenue<br>Albany, NY 12203</span>
      </li>
    </ul>
  </section>

  <section class="card card--back" aria-label="Card back">
    <svg class="card__shapes" viewBox="0 0 900 540" aria-hidden="true">
      <rect width="900" height="540" fill="var(--mist)"/>
      <path d="M222 0 C222 120 300 220 420 304 L92 540 L900 540 L900 0 Z" fill="var(--navy)"/>
      <path d="M238 0 C240 120 316 220 430 302 L150 540 L900 540 L900 0 Z" fill="var(--plum)"/>
      <path d="M832 76 C660 96 540 196 430 302 C560 196 680 110 832 76 Z" fill="var(--navy)" stroke="var(--navy)" stroke-width="3"/>
    </svg>

    <div class="site-link">
      <svg width="18" height="18" viewBox="0 0 24 24" aria-hidden="true" fill="none" stroke="var(--white)" stroke-width="1.8">
        <circle cx="12" cy="12" r="9.5"/>
        <ellipse cx="12" cy="12" rx="4.2" ry="9.5"/>
        <line x1="2.5" y1="12" x2="21.5" y2="12"/>
      </svg>
      <span>calmbriefcounsel.net</span>
    </div>

    <div class="brand-seal">
      <span class="brand-seal__name">CALM BRIEF<br>COUNSEL</span>
    </div>
  </section>

</main>
</body>
</html>
```